A Book Cover For a Book Called "Tamsire"

Attached are two files for the ISBN bar graph for the print version of the cover! Same image, just two different formats.
Updates

Project Deadline Extended Reason: We'd like to see a few more designs, and work with a few of the designs already submitted. Added Tuesday, October 24, 2017

Target Market(s)

young adult female, parents

Colors

Designer to choose colors to be used in the design.

```html
<!DOCTYPE html>
<html lang="en">
<head>
<meta charset="utf-8">
<title>Tamsire – A memoir</title>
<link rel="stylesheet" href="https://fonts.googleapis.com/css2?family=Parisienne&family=Montserrat:wght@300;400&display=swap">
<style>
  :root {
    --page-bg: #e4e4e4;
    --cover-navy: #06061c;
    --cover-navy-deep: #020210;
    --satin-light: #efe3cf;
    --satin-mid: #b99c78;
    --satin-shadow: #4a3b2c;
    --barre: rgba(150, 120, 90, 0.45);
    --text-white: #ffffff;
  }
  * { margin: 0; padding: 0; box-sizing: border-box; }
  html, body {
    width: 1200px;
    height: 800px;
    overflow: hidden;
    background: var(--page-bg);
  }
  .canvas {
    position: relative;
    width: 1200px;
    height: 800px;
  }
  .book-cover {
    position: absolute;
    left: 365px;
    top: 40px;
    width: 470px;
    height: 720px;
    background: linear-gradient(180deg, var(--cover-navy) 0%, var(--cover-navy-deep) 100%);
    overflow: hidden;
    box-shadow: 0 6px 18px rgba(0, 0, 0, 0.18);
  }
  .cover-photo {
    position: absolute;
    left: 90px;
    top: 100px;
    width: 380px;
    height: 380px;
    background:
      radial-gradient(ellipse 40% 30% at 35% 50%, var(--satin-light) 0%, var(--satin-mid) 45%, transparent 75%),
      radial-gradient(ellipse 38% 34% at 68% 40%, var(--satin-mid) 0%, var(--satin-shadow) 55%, transparent 80%);
    opacity: 0.95;
  }
  .barre-line {
    position: absolute;
    left: 0;
    top: 500px;
    width: 100%;
    height: 0;
    border-top: 3px solid var(--barre);
    transform: rotate(5deg);
    transform-origin: left center;
  }
  .author-credit {
    position: absolute;
    left: 46px;
    top: 42px;
    font-family: "Montserrat", sans-serif;
    font-weight: 300;
    font-size: 17px;
    line-height: 1.3;
    color: var(--text-white);
  }
  .title-block {
    position: absolute;
    left: 38px;
    top: 450px;
    width: 420px;
    color: var(--text-white);
  }
  .book-title {
    font-family: "Parisienne", cursive;
    font-weight: 400;
    font-size: 118px;
    line-height: 1;
  }
  .book-subtitle {
    margin-top: 2px;
    padding-left: 140px;
    font-family: "Montserrat", sans-serif;
    font-weight: 300;
    font-size: 28px;
  }
</style>
</head>
<body>
  <div class="canvas">
    <div class="book-cover">
      <div class="cover-photo" role="img" aria-label="Photograph of a pair of satin pointe shoes with ribbons on a dark background"></div>
      <div class="barre-line"></div>
      <p class="author-credit">Marlow Hayes<br>with Petra Lind</p>
      <div class="title-block">
        <h1 class="book-title">Tamsire</h1>
        <p class="book-subtitle">A memoir</p>
      </div>
    </div>
  </div>
</body>
</html>
```